Castelvarro Winery

Create 2 page flyer- front of back- showcasing each wine release and map of vineyards in the Toreno Ridge Uplands. If you can make it one page, event better.

Attached you'll find the Castelvarro Logo, Toreno Ridge Uplands vineyard map that showcases the RT Vineyard (need to remove Balu wine label) and an example of my labels. And the text that goes with this.

you can also visit my website at castelvarrowinery.example

Target Market(s)

Wine consumers. This is my flyer for wine tastings.

Industry/Entity Type

Event

Requirements
Must have
• All things contained within the Castelvarro Wines_2011_2012_v3 document
Nice to have
• Map of the Toreno Ridge Uplands.

```html
<!DOCTYPE html>
<html lang="en">
<head>
<meta charset="utf-8">
<title>Castelvarro – Wine Release Sheet</title>
<link rel="stylesheet" href="https://fonts.googleapis.com/css2?family=Josefin+Sans:wght@400&family=EB+Garamond:ital,wght@0,400;0,700;1,400&display=swap">
<style>
  :root {
    --paper: #fdfcf2;
    --ink: #1e1e1e;
    --wine: #b3262c;
    --muted: #7a7a7a;
    --footer: #000000;
    --footer-ink: #ffffff;
  }
  * { margin: 0; padding: 0; box-sizing: border-box; }
  html, body { width: 848px; height: 1200px; overflow: hidden; background: var(--paper); }
  .sheet {
    position: relative; width: 848px; height: 1200px;
    background: var(--paper); color: var(--ink);
    font-family: "EB Garamond", Georgia, serif;
  }
  .brand { position: absolute; left: 0; right: 0; top: 70px; text-align: center; }
  .brand-name {
    font-family: "Josefin Sans", Arial, sans-serif; font-weight: 400;
    font-size: 58px; letter-spacing: 2px; color: var(--ink); line-height: 1;
  }
  .brand-tagline {
    position: absolute; left: 334px; top: 150px;
    font-family: "Josefin Sans", Arial, sans-serif; font-size: 11.8px;
    letter-spacing: 0; color: var(--ink); white-space: nowrap;
  }
  .block { position: absolute; left: 120px; right: 120px; text-align: center; }
  .section-title {
    font-family: "Josefin Sans", Arial, sans-serif; font-weight: 400;
    font-size: 17.2px; letter-spacing: 0; line-height: 1;
  }
  .release { color: var(--wine); font-size: 16px; line-height: 1; }
  .release em { font-style: italic; }
  .notes { font-size: 16.2px; line-height: 21.6px; }
  .specs { font-size: 16px; line-height: 21.6px; }
  .spec-label {
    font-variant: small-caps; text-transform: lowercase; letter-spacing: 1.2px;
    color: var(--muted); font-size: 15px; margin-right: 6px;
  }
  .aside { color: var(--muted); font-style: italic; font-size: 16px; line-height: 21.4px; }
  .footer {
    position: absolute; left: 0; right: 0; bottom: 0; height: 106px;
    background: var(--footer); color: var(--footer-ink); text-align: center;
    padding-top: 20px;
  }
  .footer-name { font-weight: 700; font-size: 19px; line-height: 32px; }
  .footer-mail { font-size: 19px; line-height: 32px; }
</style>
</head>
<body>
<main class="sheet">
  <header>
    <div class="brand"><span class="brand-name">Castelvarro</span></div>
    <p class="brand-tagline">SITE DRIVEN PINOT NOIR FROM CALIFORNIA</p>
  </header>

  <section>
    <h2 class="block section-title" style="top:220px">SINGLE VINEYARD BOTTLINGS</h2>
    <p class="block release" style="top:252px">2012 &nbsp;|&nbsp; RT Vineyard &nbsp;|&nbsp; Toreno Ridge Uplands &nbsp;|&nbsp; $38</p>
    <p class="block notes" style="top:279px;left:132px;right:132px">Farmed by Dale Hoffer, the RT Vineyard is our only single vineyard bottling. The nutrient starved granite rich soils force the vines to grow deep within the earth creating fruit that’s rich with classic Pinot flavors and incredible acidity. The 2012 is gripped with ripe flavors of sour cherry, currants, blackberry. Balanced with acidity and soft tannins this powerful California Pinot Noir will drink well through 2020.</p>
    <div class="block specs" style="top:394px">
      <p><span class="spec-label">Clones</span>667 and Pommard 4</p>
      <p><span class="spec-label">Soils</span>Sandy Loom mixed with Granite and Gravel</p>
      <p><span class="spec-label">Fermentation</span>Native &nbsp;|&nbsp; 10% Whole Cluster</p>
    </div>
    <div class="block aside" style="top:462px">
      <p>Bottled Unfined and Unfiltered</p>
      <p>14% ABV</p>
    </div>
  </section>

  <section>
    <h2 class="block section-title" style="top:550px">AVA BOTTLINGS</h2>
    <p class="block release" style="top:582px">2011 &nbsp;|&nbsp; Toreno Ridge Uplands &nbsp;|&nbsp; $32</p>
    <p class="block notes" style="top:608px;left:124px;right:124px">Big, Powerful yet still highlights the unique place. The fruit was pulled from the upper blocks of the harlow vineyard. The soils are mostly clay mixed with sandy loam- creating an intense, ripe and incredible rich Pinot Noir. The fruit from this site always has more color, more intensity – a classic Powerful New World Pinot Noir.</p>
    <div class="block specs" style="top:702px">
      <p><span class="spec-label">Clones</span>667, 23, Pommard</p>
      <p><span class="spec-label">Soils</span>Clay and Sandy Loam</p>
      <p><span class="spec-label">Fermentation</span>Commercial Yeasts</p>
    </div>
    <div class="block aside" style="top:770px">
      <p>Bottled Unfined and Unfiltered</p>
      <p>14% ABV</p>
    </div>

    <p class="block release" style="top:832px">2012 &nbsp;|&nbsp; Toreno Ridge Uplands &nbsp;|&nbsp; $32 &nbsp;(<em>will release in February 2014</em>)</p>
    <p class="block notes" style="top:858px;left:122px;right:122px">This Pinot is has expressive bright red fruit flavors coupled with balanced acidity. This needs another year to mature but maintains a gorgeous ripe nose with floral accents, silky textures and a long finish that captures the essence of Pinor Noir.</p>
    <div class="block specs" style="top:931px">
      <p><span class="spec-label">Clones</span>Pommard 4, 777, 115</p>
      <p><span class="spec-label">Soils</span>Sandy Loam, Granite</p>
      <p><span class="spec-label">Fermentation</span>Native, 10% Whole Cluster</p>
    </div>
    <p class="block aside" style="top:998px">14% ABV</p>

    <p class="block release" style="top:1039px">2012 &nbsp;|&nbsp; Verano Hollow (<em>will release in spring of 2014</em>)</p>
  </section>

  <footer class="footer">
    <p class="footer-name">Castelvarro Winery LLC</p>
    <p class="footer-mail">info@castelvarrowinery.example</p>
  </footer>
</main>
</body>
</html>
```